Hello,
We’re looking for a new WordPress website for Gather Your Light, our company offering unique well-being retreats and workshops.
We currently have a website online (you can consult it : www.gatheryourlight.ch), but we now need to build a new site on WordPress — more flexible, more intuitive to manage, and better aligned with our evolving needs.

What we’re looking for:
A new userfriendly WordPress site, with:
Inspiring, elegant, and modern design
Smooth user experience on desktop and mobile
Innovative design proposals – we want to be inspired !
SEO best practices
Respect of our existing color palette
The final website will need to be set up on our existing hosting provider (details can be shared later)

Pages to Include:
- Home
- Our Story
- Our Stays - with links to 5 individual pages, each describing one of our stays in detail.
- Activities – with potential links to individual descriptive pages
- Agenda
- Our Charter
- The Team
- Contact
- Blog

Required Features:
- Space for photos and videos
- Sections for testimonials and press articles
- Blog/article layout with strong readability
- Easy-to-update backend for future content
- Newsletter sign-up (pop-up and in footer)
- Additional pop-up on/off
- “Request info” buttons
- “Booking request” buttons
- Integration of our 4 pillars - Breathe · Feel · Connect · Experience - in the design (They’re currently in the footer, but we’re open to creative suggestions)

Who we are :
Gather Your Light offers well-being and personal growth stays but with a very different spirit.
We’re not a classic wellness brand. Our approach is professional, joyful, and grounded.
We create spaces where people can take a real break — breathe, slow down, and reconnect with themselves.
During our stays, people are welcomed like friends:
with warmth, respect, and no pressure.
Each program combines practices like breathwork, movement, creativity, coaching, and massages in a relaxed, beautiful setting of the French Alps.
What makes us different:
A friendly and down-to-earth atmosphere
A wide mix of activities.
A mix of inner work and simple pleasures
Private rooms, nourishing food, and shared moments
Time to talk, to laugh, to walk, or just be silent together - and feel free to be yourself
Our guests come to pause.
They leave feeling lighter, aligned, and full of life

```html
<!DOCTYPE html>
<html lang="en">
<head>
<meta charset="utf-8">
<title>Gather Your Light — Well-being Retreats</title>
<link rel="stylesheet" href="https://fonts.googleapis.com/css2?family=Poppins:wght@400;500;600;700;800;900&display=swap">
<style>
:root{
  --navy:#1b3c93;
  --blue:#1f45a3;
  --teal:#6cc6c1;
  --orange:#f1bb79;
  --violet:#6d87e2;
  --pink:#e15ca9;
  --red:#ef4a56;
  --text:#5a6378;
  --white:#ffffff;
  --line:#d9dde6;
}
*{box-sizing:border-box;margin:0;padding:0}
html,body{width:1200px;height:4468px;overflow:hidden}
body{position:relative;font-family:"Poppins",sans-serif;color:var(--text);background:var(--white)}
.abs{position:absolute}
/* header */
.site-header{left:0;top:0;width:1200px;height:76px;background:var(--white);z-index:5}
.brand{left:88px;top:24px;font-size:21px;font-weight:700;color:var(--navy);letter-spacing:.2px;white-space:nowrap}
.main-nav{left:316px;top:0;height:76px;display:flex;align-items:center;gap:22px;font-size:12px;color:var(--navy);font-weight:500;white-space:nowrap}
.btn{display:inline-flex;align-items:center;justify-content:center;background:var(--teal);color:var(--white);font-weight:700;font-size:10px;letter-spacing:.3px;border-radius:30px;text-transform:uppercase;white-space:nowrap}
.booking{left:973px;top:17px;width:137px;height:42px}
/* hero */
.hero-photo{left:0;top:76px;width:1200px;height:760px;background:linear-gradient(135deg,#c9a233 0%,#d7b745 30%,#a9bd3e 60%,#6f9a2c 100%)}
.hero-title{left:132px;top:195px;font-size:110px;font-weight:900;line-height:100px;color:var(--white);letter-spacing:-1px}
.hero-sub{left:132px;top:522px;font-size:32px;font-weight:600;color:var(--white)}
/* history */
.history-art{left:0;top:790px;width:600px;height:555px;background:radial-gradient(circle at 55% 50%,var(--teal) 0 22%,#e9f7f6 23% 60%,#fff 61%)}
h2{font-weight:800;color:var(--navy);font-size:47px;letter-spacing:-.5px}
.history-title{left:692px;top:930px}
.history-copy{left:692px;top:1003px;width:372px;font-size:11.5px;line-height:19px}
.history-copy p{margin-bottom:18px}
.history-btn{left:694px;top:1235px;width:116px;height:41px}
/* pillars */
.pillar{width:190px;height:190px;border-radius:50%;color:var(--white);display:flex;flex-direction:column;align-items:center;justify-content:center;font-size:23px;font-weight:700;gap:8px}
.pillar svg{width:66px;height:66px}
.pillar.breathe{left:172px;top:1405px;background:var(--orange);box-shadow:0 20px 28px -10px rgba(241,187,121,.55)}
.pillar.feel{left:394px;top:1405px;background:var(--violet);box-shadow:0 20px 28px -10px rgba(109,135,226,.55)}
.pillar.connect{left:616px;top:1405px;background:var(--pink);box-shadow:0 20px 28px -10px rgba(225,92,169,.55)}
.pillar.experience{left:838px;top:1405px;background:var(--teal);box-shadow:0 20px 28px -10px rgba(108,198,193,.55)}
/* charter */
.charter-bg{left:0;top:1640px;width:1200px;height:680px;background:linear-gradient(90deg,#fff 0%,#fbf6ee 35%,#f0e3cc 60%,#e8d7b8 100%)}
.charter-photo{left:640px;top:1650px;width:560px;height:650px;background:linear-gradient(160deg,#e9ddc5 0%,#cdb89a 40%,#9fa3a0 75%,#7f9590 100%)}
.charter-title{left:175px;top:1780px}
.charter-list{left:175px;top:1868px;width:360px}
.charter-list h3{font-size:18px;font-weight:600;color:var(--navy);margin-bottom:8px}
.charter-list p{font-size:11.5px;line-height:18px;margin-bottom:28px}
.charter-btn{left:176px;top:2112px;width:116px;height:39px}
/* stays */
.stay{width:160px;text-align:center}
.stay .ico{width:108px;height:108px;border-radius:50%;margin:0 auto 16px;display:flex;align-items:center;justify-content:center}
.stay .ico svg{width:50px;height:50px}
.stay span{display:block;font-size:19px;font-weight:600;color:var(--navy);line-height:26px}
.divider{left:90px;top:2615px;width:1020px;height:1px;background:var(--line)}
/* blog */
.blog-title{left:0;top:2672px;width:1200px;text-align:center}
.card{width:260px;height:367px;top:2760px;background:var(--white);border-radius:10px;box-shadow:0 10px 30px rgba(27,60,147,.1);overflow:hidden}
.card .media{height:200px;position:relative}
.card .date{position:absolute;left:30px;bottom:14px;background:#eef0f4;color:#555;font-size:9px;padding:3px 10px;border-radius:20px}
.card .body{padding:18px 30px}
.card h4{font-size:16px;font-weight:700;color:var(--navy);line-height:22px;margin-bottom:10px}
.card p{font-size:11px;line-height:17px;margin-bottom:14px}
.card a{font-size:10px;font-weight:700;color:var(--teal);text-decoration:none;text-transform:uppercase;display:flex;align-items:center;gap:6px}
.view-all{left:531px;top:3170px;width:138px;height:42px;z-index:4}
/* testimonial */
.testi-bg{left:0;top:3230px;width:1200px;height:690px;background:linear-gradient(90deg,#e2dfda 0%,#f1efec 30%,#fff 55%)}
.testi-photo{left:70px;top:3230px;width:560px;height:660px;background:linear-gradient(180deg,#eceae6 0%,#b6c7cc 35%,#3a7f93 65%,#2d3b48 100%)}
.quote-mark{left:812px;top:3345px}
.quote{left:645px;top:3455px;width:470px;text-align:center;font-size:26px;font-weight:600;line-height:34px;color:var(--navy)}
.quote-by{left:645px;top:3605px;width:470px;text-align:center;font-size:10px;font-weight:600;letter-spacing:.5px;color:var(--text)}
.arrow{width:45px;height:45px;border-radius:50%;display:flex;align-items:center;justify-content:center;top:3649px}
/* footer */
.footer-bg{left:0;top:3800px;width:1200px;height:668px}
.news-title{left:0;top:3948px;width:1200px;text-align:center;color:var(--white);font-size:46px}
.news-form{left:288px;top:4026px;width:624px;height:52px;background:var(--white);border-radius:30px;overflow:hidden;display:flex;align-items:center}
.news-form .field{flex:1;padding-left:24px;font-size:12px;color:#777;display:flex;align-items:center;gap:10px}
.news-form .submit{width:114px;height:52px;background:var(--teal);color:var(--white);font-size:11px;font-weight:700;display:flex;align-items:center;justify-content:center}
.foot-brand{left:112px;top:4222px;font-size:30px;font-weight:700;color:var(--white);white-space:nowrap}
.foot-col{top:4143px;color:var(--white)}
.foot-col h5{font-size:16px;font-weight:700;margin-bottom:14px}
.foot-col li{list-style:none;font-size:11px;line-height:21px;color:#d6def2}
.contact-item{display:flex;gap:10px;font-size:10px;line-height:15px;color:#d6def2;margin-bottom:14px}
.contact-item b{display:block;font-weight:600;color:var(--white);font-size:9px}
.social{display:flex;gap:10px}
.social span{width:40px;height:40px;border-radius:50%;border:1px solid rgba(255,255,255,.35);background:rgba(255,255,255,.12)}
.foot-line{left:90px;top:4413px;width:1020px;height:1px;background:rgba(255,255,255,.25)}
.copyright{left:0;top:4434px;width:1200px;text-align:center;font-size:11px;color:#d6def2}
.chat{left:1134px;top:4391px;width:45px;height:45px;border-radius:50%;background:var(--teal);display:flex;align-items:center;justify-content:center}
</style>
</head>
<body>

<header class="site-header abs">
  <div class="brand abs">Gather Your Light</div>
  <nav class="main-nav abs">
    <svg width="16" height="16" viewBox="0 0 24 24" fill="#6cc6c1"><path d="M12 3 2 12h3v9h5v-6h4v6h5v-9h3z"/></svg>
    <span>Our Story</span><span>Our Stays</span><span>Activities</span><span>Agenda</span><span>Our Charter</span><span>The Team</span><span>Blog</span><span>Contact</span>
  </nav>
  <span class="btn booking abs">Booking Request</span>
</header>

<section class="hero">
  <div class="hero-photo abs" role="img" aria-label="Woman meditating cross-legged on sunlit grass"></div>
  <svg class="abs" style="left:0;top:690px" width="1200" height="150" viewBox="0 0 1200 150" preserveAspectRatio="none">
    <path d="M0 73 C120 40 240 5 360 12 C560 25 700 140 900 142 C1030 143 1120 100 1200 73 L1200 150 L0 150Z" fill="#fff"/>
  </svg>
  <h1 class="hero-title abs">Gather<br>Your<br>Light</h1>
  <p class="hero-sub abs">Imagine a space designed</p>
</section>

<section class="history">
  <div class="history-art abs" role="img" aria-label="Teal dandelion seed illustration"></div>
  <h2 class="history-title abs">Our History</h2>
  <div class="history-copy abs">
    <p>Gather Your Light is, above all, a story of men and women, a story of encounters and desire, a desire to share, a desire to refocus and a desire to breathe.</p>
    <p>Absorbed in a world that is running out of time, it has become essential to find a little personal space to take precisely the time we are so desperately running after.</p>
    <p>Through our fiduciary activities at GATHER The Horizon and GATHER The Path, we have been able to observe the growing imbalance in most of our lives and the desire...</p>
  </div>
  <span class="btn history-btn abs">Read More</span>
</section>

<section class="pillars">
  <div class="pillar breathe abs">
    <svg viewBox="0 0 64 64" fill="none" stroke="#fff" stroke-width="2.2" stroke-linecap="round"><circle cx="28" cy="20" r="10"/><path d="M18 30c-2 10 4 14 4 24M38 26c4 2 4 8 0 10M46 16l8-4M46 24h10M46 32l8 4"/></svg>
    Breathe
  </div>
  <div class="pillar feel abs">
    <svg viewBox="0 0 64 64" fill="none" stroke="#fff" stroke-width="2.2" stroke-linecap="round"><circle cx="20" cy="26" r="5"/><circle cx="32" cy="22" r="5"/><circle cx="44" cy="26" r="5"/><path d="M10 52c0-10 6-16 10-16s6 4 12 4 8-4 12-4 10 6 10 16M32 6v6M20 10l3 5M44 10l-3 5"/></svg>
    Feel
  </div>
  <div class="pillar connect abs">
    <svg viewBox="0 0 64 64" fill="none" stroke="#fff" stroke-width="2.2" stroke-linejoin="round"><path d="M10 22h12a5 5 0 1 1 8 0h10v12a5 5 0 1 0 0 8v12H10V42a5 5 0 1 0 0-8z"/><path d="M36 8h12v10a5 5 0 1 1 0 8v10"/></svg>
    Connect
  </div>
  <div class="pillar experience abs">
    <svg viewBox="0 0 64 64" fill="none" stroke="#fff" stroke-width="2.2" stroke-linecap="round"><circle cx="26" cy="28" r="7"/><path d="M12 54c0-10 6-16 14-16s10 4 12 8M38 40h14v14H38zM16 10l2 4 4 1-3 3 1 4-4-2-4 2 1-4-3-3 4-1zM32 8l2 4 4 1-3 3 1 4-4-2-4 2 1-4-3-3 4-1zM48 10l2 4 4 1-3 3 1 4-4-2-4 2 1-4-3-3 4-1z"/></svg>
    Experience
  </div>
</section>

<section class="charter">
  <div class="charter-bg abs"></div>
  <div class="charter-photo abs" role="img" aria-label="Smiling senior couple embracing by the sea"></div>
  <svg class="abs" style="left:0;top:2190px" width="1200" height="130" viewBox="0 0 1200 130" preserveAspectRatio="none">
    <path d="M0 45 C120 110 300 125 500 95 C760 55 1000 10 1200 12 L1200 130 L0 130Z" fill="#fff"/>
  </svg>
  <h2 class="charter-title abs">Our Charter</h2>
  <div class="charter-list abs">
    <h3>1. Respect and Diversity</h3>
    <p>I commit to treating myself and all other participants, speakers, and interlocutors with respect, inclusivity, listening, and kindness, without judgment or projection.</p>
    <h3>2. Sharing and Confidentiality</h3>
    <p>I promise to let everyone express themselves freely and share their opinions and experiences with respect for others and themselves.</p>
  </div>
  <span class="btn charter-btn abs">Read More</span>
</section>

<section class="stays">
  <div class="stay abs" style="left:170px;top:2375px">
    <div class="ico" style="background:var(--orange)"><svg viewBox="0 0 48 48" fill="none" stroke="#fff" stroke-width="2"><circle cx="16" cy="14" r="4"/><circle cx="32" cy="14" r="4"/><circle cx="24" cy="10" r="4"/><path d="M8 40V28h32v12M6 28h36M12 22h24"/></svg></div>
    <span>Instant<br>Workshops</span>
  </div>
  <div class="stay abs" style="left:345px;top:2375px">
    <div class="ico" style="background:var(--violet)"><svg viewBox="0 0 48 48" fill="none" stroke="#fff" stroke-width="2" stroke-linejoin="round"><path d="M24 4c2 0 3 3 3 6v8l15 9v4l-15-4v9l5 4v3l-8-2-8 2v-3l5-4v-9L6 31v-4l15-9v-8c0-3 1-6 3-6z"/></svg></div>
    <span>6-night<br>flight</span>
  </div>
  <div class="stay abs" style="left:520px;top:2375px">
    <div class="ico" style="background:var(--pink)"><svg viewBox="0 0 48 48" fill="none" stroke="#fff" stroke-width="2" stroke-linejoin="round"><path d="M24 4c2 0 3 3 3 6v8l15 9v4l-15-4v9l5 4v3l-8-2-8 2v-3l5-4v-9L6 31v-4l15-9v-8c0-3 1-6 3-6z"/></svg></div>
    <span>4-night<br>getaway</span>
  </div>
  <div class="stay abs" style="left:695px;top:2375px">
    <div class="ico" style="background:var(--teal)"><svg viewBox="0 0 48 48" fill="none" stroke="#fff" stroke-width="2" stroke-linejoin="round"><path d="M24 4c2 0 3 3 3 6v8l15 9v4l-15-4v9l5 4v3l-8-2-8 2v-3l5-4v-9L6 31v-4l15-9v-8c0-3 1-6 3-6z"/></svg></div>
    <span>2-night<br>break</span>
  </div>
  <div class="stay abs" style="left:870px;top:2375px">
    <div class="ico" style="background:var(--red)"><svg viewBox="0 0 48 48" fill="none" stroke="#fff" stroke-width="2"><rect x="8" y="10" width="32" height="30" rx="3"/><path d="M8 18h32M16 6v8M32 6v8M15 25h4M22 25h4M29 25h4M15 32h4M22 32h4M29 32h4"/></svg></div>
    <span>1 day<br>break</span>
  </div>
  <div class="divider abs"></div>
</section>

<section class="blog">
  <h2 class="blog-title abs">Latest Blog</h2>
  <article class="card abs" style="left:187px">
    <div class="media" role="img" aria-label="Lounge with fireplace and yellow cushions" style="background:linear-gradient(160deg,#8a7a66,#bfb3a0 50%,#d9c74a)"><span class="date">25-05-2025</span></div>
    <div class="body"><h4>Some Blog Heading Goes Here</h4><p>Gather Your Light is, above all, a story of men and women.</p><a>Learn More <svg width="14" height="10" viewBox="0 0 14 10" fill="none" stroke="#6cc6c1" stroke-width="1.5"><path d="M0 5h12M8 1l4 4-4 4"/></svg></a></div>
  </article>
  <article class="card abs" style="left:470px">
    <div class="media" role="img" aria-label="Woman in red jacket relaxing by a radiator" style="background:linear-gradient(160deg,#b7ab8e,#8f6c5a 55%,#7a2a3a)"><span class="date">25-05-2025</span></div>
    <div class="body"><h4>Some Blog Heading Goes Here</h4><p>Gather Your Light is, above all, a story of men and women.</p><a>Learn More <svg width="14" height="10" viewBox="0 0 14 10" fill="none" stroke="#6cc6c1" stroke-width="1.5"><path d="M0 5h12M8 1l4 4-4 4"/></svg></a></div>
  </article>
  <article class="card abs" style="left:752px">
    <div class="media" role="img" aria-label="Wooden sauna interior with bucket" style="background:linear-gradient(160deg,#e3d7c2,#c9b393 60%,#8f8478)"><span class="date">25-05-2025</span></div>
    <div class="body"><h4>Some Blog Heading Goes Here</h4><p>Gather Your Light is, above all, a story of men and women.</p><a>Learn More <svg width="14" height="10" viewBox="0 0 14 10" fill="none" stroke="#6cc6c1" stroke-width="1.5"><path d="M0 5h12M8 1l4 4-4 4"/></svg></a></div>
  </article>
</section>

<section class="testimonial">
  <div class="testi-bg abs"></div>
  <div class="testi-photo abs" role="img" aria-label="Smiling senior man jogging outdoors"></div>
  <svg class="quote-mark abs" width="136" height="88" viewBox="0 0 136 88" fill="#6cc6c1"><path d="M28 88C12 88 0 76 0 60 0 34 18 10 46 0l4 8C34 16 26 28 26 36c14 0 26 10 26 26S44 88 28 88zM102 88C86 88 74 76 74 60 74 34 92 10 120 0l4 8c-16 8-24 20-24 28 14 0 26 10 26 26s-8 26-24 26z"/></svg>
  <p class="quote abs">"This retreat was exactly what I needed — space to breathe, move, and just be. I felt seen &amp; supported every step of the way."</p>
  <p class="quote-by abs">— DANIEL T., CDL CLASS A DRIVER</p>
  <span class="arrow abs" style="left:831px;background:var(--navy)"><svg width="12" height="12" viewBox="0 0 12 12" fill="none" stroke="#fff" stroke-width="2"><path d="M8 2 4 6l4 4"/></svg></span>
  <span class="arrow abs" style="left:885px;background:var(--teal)"><svg width="12" height="12" viewBox="0 0 12 12" fill="none" stroke="#fff" stroke-width="2"><path d="m4 2 4 4-4 4"/></svg></span>
</section>

<span class="btn view-all abs">View All Blogs</span>

<footer class="site-footer">
  <svg class="footer-bg abs" viewBox="0 0 1200 668" preserveAspectRatio="none">
    <path d="M0 60 C150 30 300 40 450 80 C620 125 760 110 900 80 C1020 55 1120 35 1200 40 L1200 668 L0 668Z" fill="#1f45a3"/>
  </svg>
  <h2 class="news-title abs">Newsletter</h2>
  <div class="news-form abs">
    <div class="field"><svg width="14" height="11" viewBox="0 0 14 11" fill="none" stroke="#999" stroke-width="1.2"><rect x=".6" y=".6" width="12.8" height="9.8"/><path d="m1 1 6 5 6-5"/></svg>Enter your email address...</div>
    <div class="submit">SUBSCRIBE</div>
  </div>
  <div class="foot-brand abs">Gather Your Light</div>
  <div class="foot-col abs" style="left:439px">
    <h5>Company</h5>
    <ul><li>Our Story</li><li>Our Stays</li><li>Activities</li><li>Agenda</li><li>Our Charter</li><li>The Team</li><li>Blog</li><li>Contact</li></ul>
  </div>
  <div class="foot-col abs" style="left:581px">
    <h5>Our Stays</h5>
    <ul><li>Instant Workshops</li><li>6-night flight</li><li>4-night getaway</li><li>2-night break</li><li>1 day break</li></ul>
  </div>
  <div class="foot-col abs" style="left:747px;width:180px">
    <h5>Contact Us</h5>
    <div class="contact-item"><svg width="12" height="12" viewBox="0 0 24 24" fill="#6cc6c1"><path d="M6.6 10.8a15 15 0 0 0 6.6 6.6l2.2-2.2c.3-.3.7-.4 1-.2 1.1.4 2.3.6 3.6.6.6 0 1 .4 1 1V20c0 .6-.4 1-1 1A17 17 0 0 1 3 4c0-.6.4-1 1-1h3.5c.6 0 1 .4 1 1 0 1.3.2 2.5.6 3.6.1.3 0 .7-.2 1z"/></svg><div><b>PHONE*</b>+41 22 555 01 47</div></div>
    <div class="contact-item"><svg width="12" height="12" viewBox="0 0 24 24" fill="#6cc6c1"><path d="M2 5h20v14H2zm2 2v.5l8 5 8-5V7z"/></svg><div><b>EMAIL*</b>info@gatheryourlight.ch</div></div>
    <div class="contact-item"><svg width="12" height="12" viewBox="0 0 24 24" fill="#6cc6c1"><path d="M12 2a7 7 0 0 0-7 7c0 5 7 13 7 13s7-8 7-13a7 7 0 0 0-7-7zm0 9.5A2.5 2.5 0 1 1 12 6a2.5 2.5 0 0 1 0 5.5z"/></svg><div><b>LOCATION*</b>Gather Your Light Sàrl<br>Chemin des Prés 8<br>Building B2<br>CH - 1260 Nyon</div></div>
  </div>
  <div class="foot-col abs" style="left:945px">
    <h5>Follow Us</h5>
    <div class="social"><span></span><span></span><span></span></div>
  </div>
  <div class="foot-line abs"></div>
  <p class="copyright abs">© 2025 Gather Your Light</p>
  <span class="chat abs"><svg width="22" height="20" viewBox="0 0 22 20" fill="#fff"><path d="M11 1C5.5 1 1 4.6 1 9c0 2.2 1.1 4.2 3 5.6L3 19l4.6-2.4c1.1.3 2.2.4 3.4.4 5.5 0 10-3.6 10-8S16.5 1 11 1z"/></svg></span>
</footer>

</body>
</html>
```